Flyer für Installationsfirma für hochwertige Multimedia- und Beschallungslösungen, insbesonder in Kirchen und öffentlichen Bereichen mit Menschenansammlungen
Zielgruppe
Wir sind eine Installationsfirma für hochwertige Multimedia- und Beschallungslösungen in akustisch schwierigen Räumen. Im weiteren auch der Umbau auf LED Leuchten und dazugehörende Steuerungen. Unser Geschäft ist in Festinstallationen und Rentalbereich 'unterteilt' Weitere Infos auch auf www. brando-vex.ch
Unser Zielpublikum sind die Festinstallation für Kirchen und öffentliche Räume. Mehrzweckräume, Bühnen, Kirchen, Aulas, Bahnhofshallen, Warteräume, Konferenzräume, Tagungszentren usw. Bei diesem Flyer sollen speziell die Kirchen beworben werden. Es ist wichtig dass nebst den oben beschriebenen Leistungen auch die Displaylösung für Liedanzeigen hervorgehoben wird.
Aufgabenstellung
Ansprechender Werbe-Flyer A4 2 Seitig
Spezifische Bilder und Texte zu den versch. Angebotsbereichen für Kirchen im Anhang. Vorschläge des Grafikers sind willkommen !
Die Texte und Bilder sollten von uns angepasst und korrigiert werden können !

```html
<!DOCTYPE html>
<html lang="de">
<head>
<meta charset="utf-8">
<title>Brando Vex – Medieninstallation für Kirchenräume</title>
<link href="https://fonts.googleapis.com/css2?family=Sora:wght@300;400;600;700&display=swap" rel="stylesheet">
<style>
:root{
  --bg:#cfcfcf;
  --navy:#0d1838;
  --line:#2c3d6e;
  --cyan:#1fb6e8;
  --white:#ffffff;
  --muted:#aab4cf;
  --body:#dfe4f2;
}
*{box-sizing:border-box;margin:0;padding:0}
html,body{width:862px;height:1200px;overflow:hidden;background:var(--bg);font-family:'Sora',sans-serif}
.canvas{position:relative;width:862px;height:1200px}
.page{position:absolute;top:313px;width:405px;height:573px;background:var(--navy);color:var(--white);overflow:hidden;box-shadow:0 6px 18px rgba(0,0,0,.25)}
.page--front{left:16px}
.page--back{left:441px}

.brand{display:flex;align-items:center;gap:6px}
.brand-dot{width:18px;height:18px;border-radius:50%;border:2px solid var(--white)}
.brand-name{font-size:10px;font-weight:700;letter-spacing:.08em}

/* front */
.front-head{position:absolute;top:18px;left:22px;right:22px;display:flex;justify-content:flex-end}
.hero{position:absolute;top:46px;left:22px;right:22px;height:214px;border-radius:26px 26px 4px 4px;
  background:linear-gradient(180deg,#f3f1ec 0%,#e6dccb 45%,#b9925f 75%,#6e4a2a 100%)}
.front-copy{position:absolute;top:270px;left:22px;right:22px;display:flex;flex-direction:column}
.headline{font-size:24px;line-height:1.08;font-weight:600;color:var(--white)}
.headline .accent{color:var(--cyan)}
.subhead{margin-top:8px;display:flex;align-items:center;gap:6px;font-size:6.5px;letter-spacing:.12em;color:var(--muted)}
.subhead::before{content:"";width:14px;height:1px;background:var(--cyan)}
.intro{margin-top:8px;font-size:7px;line-height:1.55;font-weight:300;color:var(--body)}
.contact-box{margin-top:14px;width:210px;border:1px solid var(--line);border-radius:4px;padding:8px 10px}
.contact-title{font-size:6.5px;letter-spacing:.12em;color:var(--cyan);font-weight:600;padding-bottom:5px;border-bottom:1px solid var(--line);margin-bottom:6px}
.contact-grid{display:grid;grid-template-columns:1fr 1fr;gap:2px 10px;font-size:6.5px;line-height:1.5;color:var(--body)}
.contact-grid strong{font-weight:600;color:var(--white)}
.page-foot{position:absolute;bottom:16px;left:22px;right:22px;display:flex;justify-content:space-between;font-size:6px;color:var(--muted);border-top:1px solid var(--line);padding-top:6px}

/* back */
.back-head{position:absolute;top:22px;left:22px;right:22px;display:flex;justify-content:space-between}
.back-title{display:flex;gap:10px;align-items:flex-start}
.title-ring{width:34px;height:34px;border-radius:50%;border:3px solid var(--white);margin-top:4px}
.back-title h2{font-size:27px;line-height:1.02;font-weight:600}
.back-title h2 span{color:var(--cyan)}
.back-contact{font-size:5.8px;line-height:1.6;color:var(--muted);margin-top:4px}
.back-contact strong{color:var(--white);font-weight:600;letter-spacing:.08em}

.services{position:absolute;top:100px;left:22px;right:22px}
.service{display:flex;gap:12px;height:108px;align-items:center}
.service--flip{flex-direction:row-reverse}
.service-photo{flex:0 0 148px;height:78px;border-radius:6px}
.service-body{flex:1}
.service-head{display:flex;align-items:center;gap:6px;margin-bottom:6px}
.service-icon{width:16px;height:16px;border-radius:50%;background:var(--cyan);display:flex;align-items:center;justify-content:center}
.service-head h3{font-size:10px;font-weight:600;white-space:nowrap}
.service-head .rule{flex:1;height:1px;background:var(--line)}
.service-body p{font-size:6.6px;line-height:1.55;font-weight:300;color:var(--body)}

.photo-sound{background:linear-gradient(160deg,#efe6d4,#b98c55 70%,#7a5532)}
.photo-led{background:linear-gradient(160deg,#f4c7f0,#b38ee0 50%,#5d4a9c)}
.photo-control{background:linear-gradient(160deg,#2b3b1e,#6fae3a 55%,#1d2a14)}
.photo-lyrics{background:linear-gradient(160deg,#1b1b2a,#5a3f22 55%,#e0a445)}
</style>
</head>
<body>
<div class="canvas">

  <section class="page page--front">
    <header class="front-head">
      <div class="brand"><span class="brand-dot"></span><span class="brand-name">BRANDO VEX</span></div>
    </header>
    <div class="hero" role="img" aria-label="Foto: hell erleuchteter Kircheninnenraum mit Holzbänken und Altar"></div>
    <div class="front-copy">
      <h1 class="headline"><span class="accent">Zeitgemässe<br>Medieninstallation</span><br>für Kirchenräume</h1>
      <p class="subhead">MULTIMEDIA-INSTALLATION IN KIRCHEN UND EVENTRÄUMEN</p>
      <p class="intro">Wir planen und installieren hochwertige Multimedia- und Beschallungslösungen für akustisch anspruchsvolle Räume. Von der Tonanlage über moderne LED-Beleuchtung bis zur digitalen Liedanzeige – alles aus einer Hand, zuverlässig und genau auf Ihre Kirche abgestimmt. Wir beraten Sie gerne persönlich vor Ort.</p>
      <div class="contact-box">
        <div class="contact-title">KONTAKTIEREN SIE UNS</div>
        <div class="contact-grid">
          <span><strong>BRANDO VEX GmbH</strong></span><span>+41 52 000 12 34</span>
          <span>Industriestrasse 12</span><span>info@brando-vex.ch</span>
          <span>8400 Winterthur</span><span>www. brando-vex.ch</span>
        </div>
      </div>
    </div>
    <footer class="page-foot"><span>brando-vex.ch</span><span>+41 52 000 12 34</span><span>info@brando-vex.ch</span></footer>
  </section>

  <section class="page page--back">
    <header class="back-head">
      <div class="back-title">
        <span class="title-ring"></span>
        <h2>Unsere<br><span>Leistungen</span></h2>
      </div>
      <div class="back-contact">
        <strong>BRANDO VEX GmbH</strong><br>
        Industriestrasse 12<br>
        8400 Winterthur<br>
        +41 52 000 12 34<br>
        info@brando-vex.ch
      </div>
    </header>

    <div class="services">
      <article class="service">
        <div class="service-photo photo-sound" role="img" aria-label="Foto: Kirchenraum mit unauffälligen Lautsprechern"></div>
        <div class="service-body">
          <div class="service-head"><span class="service-icon"><svg width="8" height="8" viewBox="0 0 8 8"><path d="M1 3h2l2-2v6L3 5H1z" fill="#fff"/></svg></span><h3>Beschallung</h3><span class="rule"></span></div>
          <p>Klare Sprachverständlichkeit auch in halligen Räumen. Wir planen und installieren Beschallungsanlagen, die sich dezent in die Architektur Ihrer Kirche einfügen.</p>
        </div>
      </article>
      <article class="service service--flip">
        <div class="service-photo photo-led" role="img" aria-label="Foto: Kirche mit farbiger LED-Beleuchtung"></div>
        <div class="service-body">
          <div class="service-head"><span class="service-icon"><svg width="8" height="8" viewBox="0 0 8 8"><circle cx="4" cy="3.5" r="2.2" fill="#fff"/><rect x="3" y="6" width="2" height="1.4" fill="#fff"/></svg></span><h3>LED-Beleuchtung</h3><span class="rule"></span></div>
          <p>Umbau auf energiesparende LED-Leuchten mit passenden Steuerungen. Stimmungsvolle Lichtszenen für Gottesdienste, Konzerte und besondere Anlässe.</p>
        </div>
      </article>
      <article class="service">
        <div class="service-photo photo-control" role="img" aria-label="Foto: Steuerpult mit Bildschirm für Licht und Ton"></div>
        <div class="service-body">
          <div class="service-head"><span class="service-icon"><svg width="8" height="8" viewBox="0 0 8 8"><rect x="1" y="1.5" width="6" height="1" fill="#fff"/><rect x="1" y="3.5" width="6" height="1" fill="#fff"/><rect x="1" y="5.5" width="6" height="1" fill="#fff"/></svg></span><h3>Integration | Steuerung</h3><span class="rule"></span></div>
          <p>Alle Systeme bequem über ein Touchpanel bedienen. Wir verbinden Ton, Licht und Video zu einer einfachen, intuitiven Gesamtlösung.</p>
        </div>
      </article>
      <article class="service service--flip">
        <div class="service-photo photo-lyrics" role="img" aria-label="Foto: Gemeinde vor einer Leinwand mit Liedtext"></div>
        <div class="service-body">
          <div class="service-head"><span class="service-icon"><svg width="8" height="8" viewBox="0 0 8 8"><rect x="1" y="1.5" width="6" height="4" fill="none" stroke="#fff" stroke-width="1"/><rect x="3.5" y="5.5" width="1" height="1.5" fill="#fff"/></svg></span><h3>Lieder | Textanzeige</h3><span class="rule"></span></div>
          <p>Digitale Liedanzeigen und Textprojektionen für Ihre Gemeinde. Gut lesbar, einfach zu bedienen und flexibel für jeden Anlass einsetzbar.</p>
        </div>
      </article>
    </div>
    <footer class="page-foot"><span>brando-vex.ch</span><span>BRANDO VEX GmbH</span><span>+41 52 000 12 34</span></footer>
  </section>

</div>
</body>
</html>
```